International Life Insurer Needs a Web Design

What We Do: We are a boutique financial services firm specializing in solutions that financial services professionals can integrate into comprehensive wealth preservation strategies for their clients. Strategies we provide may run the spectrum from simple life insurance products to complex cases with very sophisticated and intricate solutions.

Industry Type: Financial & Insurance

Top Things to Communicate Through Our Web Design:
#1 Ultra High Net Worth
#2 INTERNATIONAL
#3 Private Banking
#4 Expertise
________________________________________
Our Target Audience:
Financial institutions/private banks who have high net worth/ultra high net worth international clients looking for unparalleled expertise in wealth preservation, taxation, and business insurance. The audience is the financial service professional, not the end client of the financial services. We will direct the professional to the site.
We Like These Designs. (fonts, colors, style):
Simple font, clean, modern, contemporary, blue colors
NOT stodgy, old, gothic, etc.

Secondarily, we’d like to also create a small tri-fold brochure incorporating the web elements (design, text), so the ability to transfer the design to print might be a plus.
Updates

Target Market(s)

Financial services professionals catering to their ultra high net worth clients

Industry/Entity Type

Life Insurance

Requirements
Must have
• Our logo (see uploaded file)
Nice to have
• the existing website includes some text that could be reviewed for ideas and incorporated into the design: http://harborlinecoveragepartners.example/

```html
<!DOCTYPE html>
<html lang="en">
<head>
<meta charset="utf-8">
<title>Harborline Coverage Partners – Case Studies</title>
<link rel="stylesheet" href="https://fonts.googleapis.com/css2?family=Arimo:wght@400;700&display=swap">
<style>
  :root {
    --page: #ffffff;
    --navy-deep: #002f66;
    --navy: #003a7a;
    --blue: #1b63b9;
    --blue-tab: #1a5fb3;
    --footer: #002a5a;
    --white: #ffffff;
    --link-blue: #1a5fb3;
    --logo-blue: #1f3f84;
    --photo-light: #f4f5f7;
    --photo-mid: #d8dde6;
    --photo-dark: #8e9ab0;
  }
  * { box-sizing: border-box; margin: 0; padding: 0; }
  html, body { width: 1200px; height: 800px; overflow: hidden; background: var(--page); }
  body { position: relative; font-family: "Arimo", Arial, sans-serif; color: var(--white); }

  /* ---------- Main page ---------- */
  .site { position: absolute; left: 22px; top: 60px; width: 851px; height: 682px; }
  .site-header { position: absolute; left: 0; top: 0; width: 851px; height: 212px; background: var(--page); }
  .brand { position: absolute; left: 30px; top: 28px; display: flex; align-items: center; gap: 12px; }
  .brand-mark { width: 60px; height: 70px; background: var(--logo-blue); }
  .brand-name { color: var(--logo-blue); font-size: 27px; line-height: 28px; font-weight: 400; }
  .hero-photo { position: absolute; left: 410px; top: 0; width: 441px; height: 212px;
    background: linear-gradient(120deg, var(--photo-light) 0%, var(--photo-mid) 55%, var(--photo-dark) 100%); }

  .site-body { position: absolute; left: 0; top: 212px; width: 851px; height: 470px; background: var(--navy); }
  .site-footer { position: absolute; left: 0; bottom: 0; width: 851px; height: 48px; background: var(--footer); }

  .main-nav { position: absolute; top: 9px; left: 32px; height: 41px; }
  .nav-tab { position: absolute; top: 0; height: 41px; background: var(--blue-tab);
    display: flex; align-items: center; justify-content: center; font-size: 16px; }
  .nav-tab.is-active { font-weight: 700; }

  .content { position: absolute; left: 32px; top: 58px; width: 787px; height: 356px; background: var(--blue); }
  .page-title { position: absolute; left: 83px; top: 56px; font-size: 19px; font-weight: 400; }
  .case { position: absolute; left: 43px; top: 115px; width: 690px; font-size: 15px; line-height: 19px; }
  .case-title { font-size: 15px; font-weight: 700; margin-bottom: 21px; }
  .case-label { display: block; margin-top: 0; }
  .case p { margin-bottom: 19px; }

  .submenu { position: absolute; left: 532px; top: 0; width: 255px; list-style: none; }
  .submenu li { height: 24px; background: var(--white); color: var(--link-blue); font-size: 13px;
    padding: 3px 0 0 10px; border-bottom: 2px solid var(--blue); }

  /* ---------- Thumbnails ---------- */
  .thumb { position: absolute; left: 896px; width: 279px; height: 222px; }
  .thumb-header { position: absolute; inset: 0 0 auto 0; height: 70px; background: var(--page); }
  .thumb .brand { left: 10px; top: 9px; gap: 4px; }
  .thumb .brand-mark { width: 20px; height: 22px; }
  .thumb .brand-name { font-size: 9px; line-height: 9px; }
  .thumb-photo { position: absolute; left: 133px; top: 0; width: 146px; height: 70px;
    background: linear-gradient(120deg, var(--photo-light) 0%, var(--photo-mid) 55%, var(--photo-dark) 100%); }
  .thumb-body { position: absolute; left: 0; top: 70px; width: 279px; height: 152px; background: var(--navy); }
  .thumb-footer { position: absolute; left: 0; bottom: 0; width: 279px; height: 15px; background: var(--footer); }
  .thumb-nav { position: absolute; top: 2px; left: 0; }
  .thumb-nav span { position: absolute; top: 0; height: 14px; background: var(--blue-tab); font-size: 5.5px;
    display: flex; align-items: center; justify-content: center; }
  .thumb-content { position: absolute; left: 10px; top: 19px; width: 259px; height: 115px; background: var(--blue); }
  .thumb-case { position: absolute; left: 15px; top: 37px; width: 225px; font-size: 5px; line-height: 6.5px; }
  .thumb-case h3 { font-size: 5.5px; font-weight: 700; margin-bottom: 7px; }
  .thumb-case p { margin-bottom: 4px; }
  .scrollbar { position: absolute; right: 11px; top: 36px; width: 2px; height: 72px; background: var(--white); }
  .scrollbar::before { content: ""; position: absolute; left: -1px; top: 0; width: 4px; height: 22px; background: var(--navy-deep); }
</style>
</head>
<body>

<section class="site">
  <header class="site-header">
    <div class="brand">
      <div class="brand-mark"></div>
      <div class="brand-name">Harborline Coverage<br>Partners</div>
    </div>
    <div class="hero-photo" role="img" aria-label="Photo of business people reviewing financial documents with pens"></div>
  </header>

  <div class="site-body">
    <nav class="main-nav">
      <div class="nav-tab is-active" style="left:0;width:134px">Home</div>
      <div class="nav-tab" style="left:142px;width:169px">About Us</div>
      <div class="nav-tab" style="left:319px;width:293px">Solutions for Diverse Needs</div>
      <div class="nav-tab" style="left:620px;width:167px">Case Studies</div>
    </nav>

    <main class="content">
      <h1 class="page-title">Case Studies</h1>
      <article class="case">
        <h2 class="case-title">Central American Executive</h2>
        <p><span class="case-label">Situation:</span>Central American executive transferred to the US for 3 years.</p>
        <p><span class="case-label">Action:</span>Successfully implemented a US-compliant DVA prior to his move to the US.</p>
        <p><span class="case-label">Results:</span>Saved the client the 1% excise tax and provide tax deferral on the policy’s underlying investments while being a US-taxed resident.</p>
      </article>
      <ul class="submenu">
        <li>Central American Executive</li>
        <li>South American Citizen, Swiss Resident</li>
        <li>Venezuelan Resident</li>
        <li>South American Partners</li>
        <li>U.S. Children of South American Parents</li>
        <li>Mexican and Brazilian Clients</li>
      </ul>
    </main>
    <footer class="site-footer"></footer>
  </div>
</section>

<section class="thumb" style="top:60px">
  <div class="thumb-header">
    <div class="brand"><div class="brand-mark"></div><div class="brand-name">Harborline Coverage<br>Partners</div></div>
    <div class="thumb-photo" role="img" aria-label="Photo of business people reviewing financial documents"></div>
  </div>
  <div class="thumb-body">
    <div class="thumb-nav">
      <span style="left:10px;width:44px">Home</span><span style="left:57px;width:55px">About Us</span><span style="left:115px;width:99px">Solutions for Diverse Needs</span><span style="left:217px;width:52px">Case Studies</span>
    </div>
    <div class="thumb-content">
      <div class="thumb-case">
        <h3>Central American Executive</h3>
        <p>Situation:<br>Central American executive transferred to the US for 3 years.</p>
        <p>Action:<br>Successfully implemented a US-compliant DVA prior to his move to the US.</p>
        <p>Results:<br>Saved the client the 1% excise tax and provide tax deferral on the policy’s underlying investments while being a US-taxed resident.</p>
      </div>
      <div class="scrollbar"></div>
    </div>
    <div class="thumb-footer"></div>
  </div>
</section>

<section class="thumb" style="top:289px">
  <div class="thumb-header">
    <div class="brand"><div class="brand-mark"></div><div class="brand-name">Harborline Coverage<br>Partners</div></div>
    <div class="thumb-photo" role="img" aria-label="Photo of business people reviewing financial documents"></div>
  </div>
  <div class="thumb-body">
    <div class="thumb-nav">
      <span style="left:10px;width:44px">Home</span><span style="left:57px;width:55px">About Us</span><span style="left:115px;width:99px">Solutions for Diverse Needs</span><span style="left:217px;width:52px">Case Studies</span>
    </div>
    <div class="thumb-content">
      <div class="thumb-case">
        <h3>South American Citizen, Swiss Resident</h3>
        <p>Situation:<br>South American citizen, Swiss resident with a US $30MM inheritance tax liability in his home country.</p>
        <p>Action:<br>Recommended a 10 pay Guaranteed Universal Life policy, held under a home country compliant structure.</p>
        <p>Results:<br>Death benefit will be paid income and inheritance tax free.</p>
      </div>
      <div class="scrollbar"></div>
    </div>
    <div class="thumb-footer"></div>
  </div>
</section>

<section class="thumb" style="top:518px">
  <div class="thumb-header">
    <div class="brand"><div class="brand-mark"></div><div class="brand-name">Harborline Coverage<br>Partners</div></div>
    <div class="thumb-photo" role="img" aria-label="Photo of business people reviewing financial documents"></div>
  </div>
  <div class="thumb-body">
    <div class="thumb-nav">
      <span style="left:10px;width:44px">Home</span><span style="left:57px;width:55px">About Us</span><span style="left:115px;width:99px">Solutions for Diverse Needs</span><span style="left:217px;width:52px">Case Studies</span>
    </div>
    <div class="thumb-content">
      <div class="thumb-case">
        <h3>Venezuelan Resident</h3>
        <p>Situation:<br>Venezuelan resident purchased a $20MM coop apartment in NYC and due to the coop regulations was unable to buy the property under a structure.</p>
        <p>Action:<br>Since the client was unsure as to how long she would keep the apartment, we implemented a 30 year term policy.</p>
        <p>Results:</p>
      </div>
      <div class="scrollbar"></div>
    </div>
    <div class="thumb-footer"></div>
  </div>
</section>

</body>
</html>
```